Accountancy firm needs clean and simple website and optional logo

We need a logo and basic wordpress website design for a Sydney based accountancy firm.
We need a clean and simple logo and website, based on the accounting/finance/tax industry. Simple, credible and official colors.
The logo is expected to be so simple that we have combined into the one job.
If you submit a logo design and we choose it along with someone else's website design you will be paid a bonus of $60. The website design will still win the competition as per normal.
Current website is old and terrible but gives you an idea of the sitemap (super simple) and what they do: www.helmwick.com.au
We want original different to normal template looking designs.
We like videos, and like http://www.marbeckers.com.au/
Feel free to go to reelmoss and use some videos from there.
We are based in Sydney Australia and in the field of taxation and accounting
We want a clean, formal, credible site, limited pages.
The project is guaranteed, so go for it.
Dorrit & Associates
1 page

```html
<!DOCTYPE html>
<html lang="en">
<head>
<meta charset="utf-8">
<title>Dorrit &amp; Associates — Tax Accountants</title>
<link href="https://fonts.googleapis.com/css2?family=Rokkitt:wght@300;400;500;700&display=swap" rel="stylesheet">
<style>
  :root {
    --blue: #0a9cf5;
    --blue-deep: #1a88dd;
    --ink: #1b1b1b;
    --text: #444;
    --muted: #666;
    --line: #e3e3e3;
    --panel: #f1f1f1;
    --header: #f5f5f5;
    --white: #fff;
  }
  * { box-sizing: border-box; margin: 0; padding: 0; }
  html, body { width: 954px; height: 1200px; overflow: hidden; }
  body { position: relative; background: var(--white); font-family: "Rokkitt", Georgia, serif; color: var(--text); }

  .site-header { position: absolute; top: 0; left: 0; width: 954px; height: 88px; background: var(--header); border-bottom: 1px solid #dcdcdc; }
  .brand { position: absolute; left: 38px; top: 10px; display: flex; align-items: center; gap: 14px; }
  .brand-mark { width: 68px; height: 68px; border-radius: 50%; border: 3px solid #8a8a8a; }
  .brand-name { font-size: 25px; font-weight: 500; color: var(--blue-deep); letter-spacing: -0.3px; line-height: 1; }
  .brand-tag { font-size: 12px; letter-spacing: 7px; color: #777; margin-top: 4px; }
  .main-nav { position: absolute; top: 36px; right: 41px; display: flex; gap: 58px; font-size: 13px; }
  .main-nav a { color: #555; text-decoration: none; }
  .main-nav a.is-active { color: var(--blue); border-bottom: 2px solid var(--blue); padding-bottom: 6px; }

  .hero { position: absolute; top: 88px; left: 0; width: 954px; height: 441px; }
  .hero-photo { position: absolute; inset: 0; background: linear-gradient(90deg, #8d9aa4 0%, #6b7884 35%, #526173 65%, #465466 100%); }
  .hero-photo::after { content: ""; position: absolute; inset: 0; background: linear-gradient(180deg, rgba(70,90,110,.2), rgba(60,60,70,.35)); }
  .hero-content { position: absolute; top: 148px; left: 0; width: 954px; text-align: center; color: var(--white); }
  .hero-title { font-weight: 400; font-size: 38px; line-height: 45px; letter-spacing: .5px; }
  .hero-lead { width: 620px; margin: 14px auto 0; font-size: 10.5px; line-height: 13px; }
  .btn { display: inline-block; background: var(--blue); color: var(--white); font-size: 11px; text-decoration: none; text-align: center; }
  .hero .btn { margin-top: 20px; width: 99px; height: 29px; line-height: 29px; }
  .hero-arrow { position: absolute; top: 186px; }
  .hero-arrow.prev { left: 22px; }
  .hero-arrow.next { right: 22px; }
  .hero-shadow { position: absolute; top: 529px; left: 0; width: 954px; height: 26px; background: radial-gradient(ellipse 60% 100% at 50% 0%, rgba(0,0,0,.12), rgba(0,0,0,0)); }

  .services-title { position: absolute; top: 576px; left: 0; width: 954px; text-align: center; font-size: 36px; font-weight: 400; color: var(--ink); }
  .services-title span { color: var(--blue); }
  .service-card { position: absolute; top: 660px; width: 285px; height: 218px; border: 1px solid var(--line); text-align: center; }
  .service-card.is-featured { border-color: var(--blue); }
  .service-icon { display: block; margin: 24px auto 0; }
  .service-name { margin-top: 18px; font-size: 18px; font-weight: 400; color: var(--ink); }
  .service-desc { width: 250px; margin: 6px auto 0; font-size: 10px; line-height: 13px; color: var(--muted); }
  .service-link { display: inline-block; margin-top: 9px; font-size: 10.5px; color: #333; text-decoration: none; }
  .is-featured .service-link { color: var(--blue); }

  .info-band { position: absolute; top: 913px; left: 0; width: 954px; height: 218px; background: var(--panel); }
  .info-col { position: absolute; top: 34px; }
  .info-col h3 { font-size: 14px; font-weight: 400; color: var(--blue); margin-bottom: 14px; }
  .info-col p { font-size: 10px; line-height: 15px; color: #333; text-align: justify; }
  .col-about { left: 46px; width: 288px; }
  .col-about .btn { position: absolute; top: 145px; left: -2px; width: 100px; height: 30px; line-height: 30px; }
  .col-news { left: 408px; width: 268px; padding-top: 1px; }
  .col-news p { line-height: 13.5px; }
  .email-field { position: absolute; top: 91px; left: 2px; width: 266px; height: 29px; background: var(--white); border: 1px solid #e6e6e6; font-size: 8px; color: #aaa; padding: 9px 10px; font-family: inherit; }
  .col-news .btn { position: absolute; top: 131px; left: 2px; width: 266px; height: 29px; line-height: 29px; }
  .divider { position: absolute; top: 30px; width: 1px; height: 150px; background: #e1e1e1; }
  .col-location { left: 744px; width: 180px; }
  .social { list-style: none; }
  .social li { display: flex; align-items: center; gap: 12px; height: 30px; margin-bottom: 15px; font-size: 14px; color: #444; }
  .social li:first-child { color: var(--blue); }
  .social .dot { width: 30px; height: 30px; border-radius: 50%; border: 1px solid #999; }
  .social li:first-child .dot { background: var(--blue); border-color: var(--blue); }

  .site-footer { position: absolute; top: 1131px; left: 0; width: 954px; height: 69px; background: var(--blue); color: var(--white); text-align: center; font-size: 9px; line-height: 69px; }
</style>
</head>
<body>
  <header class="site-header">
    <div class="brand">
      <div class="brand-mark"></div>
      <div>
        <div class="brand-name">DORRIT &amp; ASSOCIATES</div>
        <div class="brand-tag">TAX ACCOUNTANTS</div>
      </div>
    </div>
    <nav class="main-nav">
      <a href="#" class="is-active">Home</a>
      <a href="#">About the Company</a>
      <a href="#">Contact Us</a>
    </nav>
  </header>

  <section class="hero">
    <div class="hero-photo" role="img" aria-label="Photo of a woman relaxing in a beach chair with a laptop by the sea"></div>
    <svg class="hero-arrow prev" width="18" height="52" viewBox="0 0 18 52"><polyline points="16,2 2,26 16,50" fill="none" stroke="#fff" stroke-width="1.5"/></svg>
    <svg class="hero-arrow next" width="18" height="52" viewBox="0 0 18 52"><polyline points="2,2 16,26 2,50" fill="none" stroke="#fff" stroke-width="1.5"/></svg>
    <div class="hero-content">
      <h1 class="hero-title">TAKE THE WORRY OUT OF TAX<br>AND BUSINESS</h1>
      <p class="hero-lead">Lorem ipsum dolor sit amet, consectetur adipiscing elit, sed do eiusmod tempor incididunt ut labore et dolore magna aliqua. Ut enim ad minim veniam, quis nostrud exercitation ullamco laboris nisi ut aliquip ex ea commodo consequat. Duis aute irure dolor in reprehenderit in voluptate velit esse cillum dolore eu fugiat nulla pariatur.</p>
      <a href="#" class="btn">Read More</a>
    </div>
  </section>
  <div class="hero-shadow"></div>

  <h2 class="services-title">Our <span>Service</span></h2>

  <article class="service-card" style="left:38px">
    <svg class="service-icon" width="64" height="64" viewBox="0 0 64 64"><circle cx="32" cy="32" r="31" fill="none" stroke="#0a9cf5" stroke-width="1.2"/><text x="32" y="45" text-anchor="middle" font-family="Arial, sans-serif" font-weight="700" font-size="36" fill="#0a9cf5">$</text></svg>
    <h3 class="service-name">Tax Planning and Returns</h3>
    <p class="service-desc">Residential loans and financing Superannuation self-managed funds Estate Planning together and succession Financial and Retirement Planning</p>
    <a href="#" class="service-link">READ MORE ▸</a>
  </article>

  <article class="service-card is-featured" style="left:334px">
    <svg class="service-icon" width="64" height="64" viewBox="0 0 64 64"><circle cx="32" cy="32" r="32" fill="#0a9cf5"/><path d="M23 18h13l7 7v21H23z" fill="none" stroke="#fff" stroke-width="2.2"/><path d="M27 30h12M27 35h12M27 40h12" stroke="#fff" stroke-width="2"/></svg>
    <h3 class="service-name">GST preparation and lodgement</h3>
    <p class="service-desc">Non resident companies and trusts Business Setup Accounting System establishment Bookkeeping and administration</p>
    <a href="#" class="service-link">READ MORE ▸</a>
  </article>

  <article class="service-card" style="left:630px">
    <svg class="service-icon" width="64" height="64" viewBox="0 0 64 64"><circle cx="32" cy="32" r="31" fill="none" stroke="#0a9cf5" stroke-width="1.2"/><path d="M16 22h10l3 3h14v5H22l-6 14z" fill="#0a9cf5"/><path d="M22 32h28l-7 14H15z" fill="#0a9cf5"/></svg>
    <h3 class="service-name">Litigation assistance</h3>
    <p class="service-desc">Business Advisory Services Asset Protection Services Business Recovery Services Specialised Investment Administration</p>
    <a href="#" class="service-link">READ MORE ▸</a>
  </article>

  <section class="info-band">
    <div class="info-col col-about">
      <h3>ABOUT US</h3>
      <p>Lorem ipsum dolor sit amet, consectetur adipiscing elit, sed do eiusmod tempor incididunt ut labore et dolore magna aliqua. Ut enim ad minim veniam, quis nostrud exercitation ullamco laboris nisi ut aliquip ex ea commodo consequat.Ut enim ad minim veniam, quis nostrud exercitation ullamco laboris nisi ut aliquip ex ea commodo consequat.</p>
      <a href="#" class="btn">READ MORE</a>
    </div>
    <div class="divider" style="left:366px"></div>
    <div class="info-col col-news">
      <h3>NEWSLETTER SIGNUP</h3>
      <p>Subscribe our newsletter to know our daily updates and offer daily updates and offer Ut enim ad minim veniam, quis nostrud exercitation</p>
      <div class="email-field">Enter your Email Id</div>
      <a href="#" class="btn">SUBSCRIBE</a>
    </div>
    <div class="divider" style="left:709px"></div>
    <div class="info-col col-location">
      <h3>LOCATION</h3>
      <ul class="social">
        <li><span class="dot"></span>Friendlink</li>
        <li><span class="dot"></span>CirclePost</li>
        <li><span class="dot"></span>Reelcast</li>
      </ul>
    </div>
  </section>

  <footer class="site-footer">@ 2015 Dorrit &amp; Associates. All right Receserved Team of Use</footer>
</body>
</html>
```